Tavrel MC celebrates 16 years

Tavrel Marketing Communication was established in 2000 by Dana Melkior and is known as one of the leading companies in Israel for Public Relations and marketing communications, with rich experience in every technology sector. Most of our client activities are based on our areas of expertise covering a wide range of Tech, High-tech, Internet and consumer devices.
We need an email signature and a banner that we will promote in our emails body and by social media. The main mesages:
16 years of success, working with global tech companies in Israel, PR and Social Media, strategic and crisis management.
See more setails: www.tavrel-mc.example

Target Market(s)

we are looking for hitech global companies that want to be promoted in Israel - by PR, Social media and more marketing communication services

Industry/Entity Type

Tech

Font styles to use
Sans Serif
Decorative

Requirements
Must have
• 1.Business and series company but colorful, creative and enthusiasm
• 2. Connection to Tavrel's logo (green) but with more colorful - not too childish
• 3. messages of global, tech and marketing communications
Nice to have
• I have no idea..
Should not have
• not too childish. we are a series company
• please don't design as tech companies - boring...

```html
<!DOCTYPE html>
<html lang="en">
<head>
<meta charset="utf-8">
<title>Tavrel MC – 16 Years Banner</title>
<link rel="stylesheet" href="https://fonts.googleapis.com/css2?family=Montserrat:wght@700;800&family=Hind:wght@500;600&family=Oswald:wght@500;600&display=swap">
<style>
  :root {
    --page-bg: #e4e4e4;
    --white: #ffffff;
    --ink: #1e1e1e;
    --green: #8cc63f;
    --green-light: #b5e03a;
    --green-dark: #6fa326;
    --map-tint: #eef0f2;
    --crowd-dark: #1b2233;
    --crowd-mid: #5a6a8a;
  }
  * { margin: 0; padding: 0; box-sizing: border-box; }
  html, body { width: 1200px; height: 1200px; overflow: hidden; }
  body { background: var(--page-bg); position: relative; }

  .banner {
    position: absolute;
    left: 131px; top: 494px;
    width: 938px; height: 218px;
    background: linear-gradient(180deg, #ffffff 0%, #f2f2f2 100%);
    overflow: hidden;
  }
  .banner__shapes { position: absolute; inset: 0; width: 100%; height: 100%; }

  .world-map {
    position: absolute; left: 10px; top: 20px; width: 320px; height: 110px;
    background: radial-gradient(ellipse at center, var(--map-tint) 0%, rgba(238,240,242,0) 70%);
  }
  .crowd {
    position: absolute; left: 0; top: 111px; width: 266px; height: 107px;
    background: linear-gradient(180deg, var(--crowd-mid) 0%, var(--crowd-dark) 70%);
    border-radius: 40px 60px 0 0;
  }

  .brand { position: absolute; left: 39px; top: 20px; display: flex; align-items: center; gap: 8px; }
  .brand__mark { width: 56px; height: 56px; background: var(--green); border-radius: 8px; }
  .brand__text { padding-top: 14px; }
  .brand__name {
    font-family: "Montserrat", sans-serif; font-weight: 700;
    font-size: 22px; line-height: 1; color: var(--green);
  }
  .brand__tagline {
    font-family: "Hind", sans-serif; font-weight: 500;
    font-size: 8.5px; color: #555; margin-top: 2px; white-space: nowrap;
  }

  .message {
    position: absolute; left: 345px; top: 30px; width: 290px; text-align: center;
  }
  .message__headline {
    font-family: "Montserrat", sans-serif; font-weight: 800;
    font-size: 42px; line-height: 40px; color: var(--ink); letter-spacing: -0.5px;
  }
  .message__headline--green { color: var(--green); }
  .message__body {
    font-family: "Hind", sans-serif; font-weight: 600;
    font-size: 15px; line-height: 20px; color: var(--ink); margin-top: 14px;
  }

  .cta { position: absolute; left: 724px; top: 44px; width: 190px; }
  .cta__title {
    font-family: "Oswald", sans-serif; font-weight: 600;
    font-size: 34px; line-height: 38px; text-transform: uppercase;
    display: block; padding-left: 26px;
  }
  .cta__title--light { color: var(--white); }
  .cta__title--dark { color: var(--ink); display: flex; align-items: center; gap: 6px; }
  .cta__arrow { width: 30px; height: 26px; }
  .cta__link {
    display: flex; align-items: center; justify-content: center;
    margin-top: 12px; width: 184px; height: 46px;
    background: linear-gradient(180deg, #ffffff 0%, #e6e6e6 100%);
    border: 3px solid #3a3a3a; border-radius: 23px;
    font-family: "Oswald", sans-serif; font-weight: 500;
    font-size: 14px; color: var(--ink); text-decoration: none; letter-spacing: -0.3px;
  }
</style>
</head>
<body>
  <section class="banner">
    <div class="world-map" role="img" aria-label="Faint world map backdrop"></div>
    <div class="crowd" role="img" aria-label="Silhouettes of a group of business people"></div>

    <svg class="banner__shapes" viewBox="0 0 938 218" preserveAspectRatio="none" aria-hidden="true">
      <defs>
        <linearGradient id="panelGreen" x1="0" y1="0" x2="0" y2="1">
          <stop offset="0" stop-color="#b9e236"/>
          <stop offset="1" stop-color="#86b92e"/>
        </linearGradient>
      </defs>
      <!-- left swoosh -->
      <path d="M342 0 C305 8 292 80 272 140 C252 200 222 214 170 218 L196 218 C248 210 272 182 287 140 C306 80 320 10 360 0 Z" fill="#1e1e1e"/>
      <path d="M360 0 C330 10 318 80 298 140 C282 192 250 212 196 218 L240 218 C290 206 304 180 314 140 C330 80 345 12 382 0 Z" fill="#8cc63f"/>
      <!-- right panel -->
      <path d="M800 0 L938 0 L938 218 L600 218 C665 210 705 188 724 130 C744 62 762 6 800 0 Z" fill="url(#panelGreen)"/>
      <path d="M786 0 C748 6 734 62 712 130 C694 186 655 210 580 218 L622 218 C684 206 712 180 726 130 C746 62 764 6 804 0 Z" fill="#1e1e1e"/>
    </svg>

    <div class="brand">
      <span class="brand__mark"></span>
      <div class="brand__text">
        <div class="brand__name">Tavrel</div>
        <div class="brand__tagline">Tavrel Marketing Communication Ltd.</div>
      </div>
    </div>

    <div class="message">
      <h1 class="message__headline">16 YEARS<br><span class="message__headline--green">OF SUCCES</span></h1>
      <p class="message__body">working with global tech companies<br>in Israel, PR &amp; Social Media, strategic<br>and crisis management</p>
    </div>

    <div class="cta">
      <span class="cta__title cta__title--light">See more</span>
      <span class="cta__title cta__title--dark">Details
        <svg class="cta__arrow" viewBox="0 0 30 26" aria-hidden="true">
          <path d="M4 16 C6 6 18 2 22 12" fill="none" stroke="#1e1e1e" stroke-width="3.5" stroke-linecap="round"/>
          <path d="M16 11 L23 20 L28 9 Z" fill="#1e1e1e"/>
        </svg>
      </span>
      <a class="cta__link" href="#">WWW.TAVREL-MC.EXAMPLE</a>
    </div>
  </section>
</body>
</html>
```